Designer Needed for Protein Label

We are looking for an experienced graphic designer to create a label for our protein supplement Quill ISOLATE 100% WHEY Protein 3LB tub. You can make it unique to our design but keep it clean and simple.

Here are some design examples that we liked, however please note ours is unflavored:

https://www.brantova.com/VelnorFit-Tundra-Protein-Powder-Chocolate/dp/K47RQWZ2NX/ref=sr_1_17_a_it?ie=UTF8&qid=1536255229&sr=8-17&keywords=protein%2Bpowder&th=1

https://www.brantova.com/dp/K93TLMQ5VB/ref=sspa_dk_detail_1?pd_rd_i=K93TLMQ5VB&pf_rd_m=QWERTYPLMNB&pf_rd_p=7c1402ab-816e-4a2c-9e3f-27a4c188f3d1&pf_rd_r=HJKWPLZNRT8VQC217DMS&pd_rd_wg=TrQ4k&pf_rd_s=desktop-dp-sims&pf_rd_t=40701&pd_rd_w=KLMN3&pf_rd_i=desktop-dp-sims&pd_rd_r=917f3a21-c2de-11e8-942a-ab17fd2249c7&th=1

Please see attachment for Quill Logo and additional label example.

Label Dimensions:
18in x 6in

Please include the following information on the label:
* Quill Icon
* ISOLATE - product name
* 100% WHEY Protein
* Unflavored
* Net WT. 3LB (1.36 KG)
* 40 Servings
* 50 Grams of Protein per serving
* XX  BCAA
* Gluten & Lactose Free
* Kosher and Halal Certified
* Non GMO
* Nutrition Facts (use as place holder)
* Ingredients
* Directions
* Barcode

```html
<!DOCTYPE html>
<html lang="en">
<head>
<meta charset="UTF-8">
<title>Quill ISOLATE 100% WHEY Protein – Label</title>
<link rel="stylesheet" href="https://fonts.googleapis.com/css2?family=Bebas+Neue&family=Oswald:wght@500&family=Roboto:wght@400&family=Kaushan+Script&display=swap">
<style>
  :root {
    --page: #ffffff;
    --label-blue: #0d3f7e;
    --band-blue: #1378b6;
    --band-edge: #0a3468;
    --gold: #f0b90b;
    --ink: #111111;
    --white: #f4f4f4;
    --badge-line: #1e8fd6;
  }
  * { margin: 0; padding: 0; box-sizing: border-box; }
  html, body {
    width: 1200px; height: 1200px; overflow: hidden;
    background: var(--page);
  }
  .label {
    position: absolute; left: 150px; top: 160px;
    width: 900px; height: 880px;
    background: var(--label-blue);
    overflow: hidden;
    font-family: "Roboto", Arial, sans-serif;
    color: var(--white);
  }
  .band {
    position: absolute; left: 0; width: 100%; height: 32px;
    background: var(--band-blue);
    border-top: 4px solid var(--band-edge);
  }
  .band--top { top: 8px; }
  .band--bottom { top: 842px; }
  .claim {
    position: absolute; top: 68px; width: 100%; text-align: center;
    font-family: "Oswald", sans-serif; font-weight: 500; font-size: 28px;
    line-height: 1.2; letter-spacing: 0.5px;
  }
  .emblem { position: absolute; left: 0; top: 0; width: 900px; height: 880px; }
  .product-name {
    position: absolute; left: 214px; top: 200px;
    font-family: "Bebas Neue", sans-serif; font-weight: 400; font-size: 124px; line-height: 1;
    color: var(--white); transform: rotate(-3deg); transform-origin: left bottom;
  }
  .brand-name {
    position: absolute; left: 232px; top: 322px; padding: 0 14px;
    font-family: "Bebas Neue", sans-serif; font-size: 196px; line-height: 0.9;
    color: var(--gold); background: var(--label-blue);
  }
  .mascot {
    position: absolute; left: 600px; top: 222px; width: 176px; height: 306px;
    background: linear-gradient(160deg, #2a2a2a, var(--ink));
    border-radius: 48% 48% 40% 40% / 35% 35% 55% 55%;
  }
  .flavor {
    position: absolute; top: 704px; width: 100%; text-align: center;
    font-family: "Kaushan Script", cursive; font-size: 56px; line-height: 1.1;
    transform: rotate(-2deg);
  }
  .net-weight {
    position: absolute; top: 796px; width: 100%; text-align: center;
    font-size: 26px; line-height: 1.2;
  }
  .protein-badge {
    position: absolute; left: 40px; top: 662px; width: 60px; height: 60px;
    border: 4px solid var(--badge-line); transform: rotate(45deg);
  }
  .protein-amount {
    position: absolute; left: 25px; top: 675px; width: 90px; text-align: center;
    font-size: 26px; line-height: 1.2; color: var(--white); transform: rotate(-6deg);
  }
  .protein-note {
    position: absolute; left: 12px; top: 762px; font-size: 22px; line-height: 1.2;
    transform: rotate(5deg); transform-origin: left top;
  }
  .servings {
    position: absolute; left: 760px; top: 774px; font-size: 22px; line-height: 1.2;
    transform: rotate(-6deg);
  }
</style>
</head>
<body>
  <main class="label">
    <div class="band band--top"></div>
    <div class="band band--bottom"></div>

    <p class="claim">Gluten &amp; Lactose Free</p>

    <svg class="emblem" viewBox="0 0 900 880" aria-hidden="true">
      <circle cx="473" cy="440" r="250" fill="none" stroke="var(--gold)" stroke-width="26"/>
      <path id="whey-arc" d="M 300 612 Q 470 630 650 566" fill="none"/>
      <text font-family="Roboto, Arial, sans-serif" font-size="38" fill="var(--white)">
        <textPath href="#whey-arc" startOffset="50%" text-anchor="middle">100% WHEY Protein</textPath>
      </text>
    </svg>

    <h1 class="product-name">ISOLATE</h1>
    <p class="brand-name">Quill</p>
    <div class="mascot" role="img" aria-label="Mascot illustration: black gas-mask character beside the brand name"></div>

    <p class="flavor">Unflavored</p>
    <p class="net-weight">Net WT. 3LB (1.36 KG)</p>

    <div class="protein-badge"></div>
    <p class="protein-amount">50g</p>
    <p class="protein-note">of Protein per serving</p>

    <p class="servings">40 Servings</p>
  </main>
</body>
</html>
```